Candidate Table Page

Need our intranet page redesigned. The layout is perfect and doesn't need to change. But the whole page doesn't seem to fit well together. Please change the font, feel, and table borders to make a more professional and easy user interface. symbols and/or icons are okay.

Target Market(s)

company staff

Industry/Entity Type

Security Guard

Coding

Coded - Design and coding required

Number of Pages Required

1 page

Font styles to use
Sans Serif

Colors
0255a3
fece3e

Requirements
Must have
• the employee information and columns
Nice to have
• icons and maybe symbols.

```html
<!DOCTYPE html>
<html lang="en">
<head>
<meta charset="utf-8">
<title>Candidate Table</title>
<link href="https://fonts.googleapis.com/css2?family=Roboto:wght@400;500;700&display=swap" rel="stylesheet">
<style>
:root{
  --brand-blue:#0255a3;
  --brand-yellow:#fece3e;
  --sidebar:#1c4a71;
  --sidebar-dark:#153a5a;
  --navy:#0c2b47;
  --text:#1e2a36;
  --muted:#6a7886;
  --row-alt:#eef6fc;
  --line:#c9d6e2;
  --danger:#e8131b;
  --pill:#cfd3d7;
  --page:#f1f3f5;
}
*{box-sizing:border-box;margin:0;padding:0}
html,body{width:1200px;height:729px;overflow:hidden}
body{font-family:"Roboto",sans-serif;color:var(--text);background:var(--page);position:relative}
.topbar{position:absolute;left:0;top:0;width:1200px;height:55px;background:#fff;display:flex;align-items:center}
.brand{width:156px;height:55px;display:flex;align-items:center;gap:6px;padding-left:9px}
.brand-mark{width:22px;height:22px;background:var(--brand-blue);border-radius:4px;flex:none}
.brand-name{font-weight:700;font-size:12.5px;line-height:1.05;color:var(--brand-blue);text-transform:uppercase}
.search-label{font-size:13px;color:#8a9096;margin-left:7px;width:143px}
.pill{height:21px;border-radius:11px;background:var(--pill);font-size:9px;color:#333;display:inline-flex;align-items:center;justify-content:space-between;padding:0 8px 0 12px;font-weight:500}
.pill::after{content:"";border:4px solid transparent;border-top:5px solid #444;border-bottom:0;margin-left:6px}
.search-input{width:113px;height:21px;border:1px solid #9aa4ad;border-radius:11px;margin:0 8px 0 7px;background:#fff}
.btn{height:21px;border-radius:11px;font-size:9px;font-weight:500;display:inline-flex;align-items:center;justify-content:center;width:49px}
.btn-find{background:var(--brand-yellow);color:#5a4300;margin-right:6px}
.btn-reset{background:var(--danger);color:#fff}
.filters{display:flex;align-items:center;margin-left:auto;margin-right:40px;gap:7px;font-size:13px;color:#8a9096}
.filters .pill{width:75px;margin-right:8px}
.logout{width:75px;height:55px;background:var(--danger);color:#fff;font-size:12px;font-weight:500;display:flex;flex-direction:column;align-items:center;justify-content:center;gap:3px}
.sidebar{position:absolute;left:0;top:55px;width:156px;height:674px;background:var(--sidebar)}
.avatar{position:absolute;left:49px;top:28px;width:52px;height:52px;border-radius:50%;background:radial-gradient(circle at 50% 40%,#c89a7a,#8a5a3c);border:2px solid #e9eef2}
.user{position:absolute;top:87px;width:156px;text-align:center}
.user-name{color:#fff;font-weight:500;font-size:11.5px}
.user-role{color:#a9bccd;font-size:8.5px;margin-top:2px}
.nav{position:absolute;top:150px;left:0;width:156px;list-style:none}
.nav-item{height:29px;display:flex;align-items:center;padding-left:10px;gap:9px;color:#fff;font-size:9.5px;font-weight:500;position:relative}
.nav-item svg{width:11px;height:11px;fill:#dfe8f0;flex:none}
.nav-item .chev{position:absolute;right:14px;font-size:9px;color:#cbd7e2}
.nav-group{background:var(--sidebar-dark);border-left:3px solid var(--brand-yellow);padding-bottom:10px;margin:4px 0 10px}
.nav-group .nav-item{padding-left:7px;height:33px}
.nav-sub{list-style:none;padding-left:31px}
.nav-sub li{font-size:8.5px;color:#c9d6e2;height:20px;line-height:20px}
.welcome{position:absolute;left:156px;width:1044px;top:97px;text-align:center}
.welcome h1{font-weight:400;font-size:19px;color:#1f4a6f}
.welcome p{font-size:10px;color:#33566f;margin-top:9px}
.welcome strong{color:#111;font-weight:500}
.candidates{position:absolute;left:175px;top:178px;width:1006px;border-collapse:collapse;table-layout:fixed;background:#fff;font-size:9.3px}
.candidates th{background:var(--navy);color:#fff;height:31px;font-weight:700;font-size:9.8px}
.candidates td{height:30.6px;text-align:center;border-bottom:1px solid var(--line);color:#222}
.candidates tbody tr:nth-child(odd) td{background:var(--row-alt)}
.candidates a{color:var(--navy);text-decoration:underline}
.reason .pill{width:50px;height:18px;font-size:8.5px}
.pager{position:absolute;left:175px;top:608px;width:1006px;height:32px;background:var(--navy);display:flex;align-items:center;padding:0 16px 0 14px;color:#fff;font-size:9.5px}
.pg{width:20px;height:20px;border-radius:50%;display:inline-flex;align-items:center;justify-content:center;margin-right:5px;font-weight:700;font-size:9px;background:var(--brand-blue);color:#fff}
.pg.nav-btn{background:#c8ced4;color:#223;font-size:8px}
.pg.current{background:var(--brand-yellow);color:#3a2c00}
.page-size{margin-left:44px;color:var(--brand-yellow);font-weight:700;display:flex;align-items:center;gap:12px}
.page-size .pill{width:38px;height:18px;padding:0 6px 0 9px}
.count{margin-left:auto;font-weight:700}
.count b{color:var(--brand-yellow)}
.footer{position:absolute;left:156px;top:706px;width:1044px;height:23px;background:#fff;display:flex;align-items:center;justify-content:space-between;padding:0 28px 0 20px;font-size:8.5px;color:#555}
</style>
</head>
<body>
<header class="topbar">
  <div class="brand"><span class="brand-mark"></span><span class="brand-name">Summit<br>Guard Services</span></div>
  <span class="search-label">Search for something...</span>
  <span class="pill" style="width:75px">Name</span>
  <span class="search-input"></span>
  <span class="btn btn-find">Find</span>
  <span class="btn btn-reset">Reset</span>
  <div class="filters">
    <span>Job:</span><span class="pill">All</span>
    <span>Status:</span><span class="pill">All</span>
    <span>Office:</span><span class="pill">All</span>
  </div>
  <div class="logout">Log out
    <svg width="11" height="10" viewBox="0 0 11 10"><path d="M0 3h5V0l6 5-6 5V7H0z" fill="#fff"/></svg>
  </div>
</header>

<aside class="sidebar">
  <div class="avatar" role="img" aria-label="Profile photo of the signed-in user"></div>
  <div class="user"><div class="user-name">Daniel Reyes</div><div class="user-role">Art Director ▾</div></div>
  <ul class="nav">
    <li class="nav-item"><svg viewBox="0 0 12 12"><path d="M3 1h6l3 4-6 6-6-6z"/></svg>Home</li>
    <li class="nav-group">
      <div class="nav-item" style="color:#fff"><svg viewBox="0 0 12 12"><path d="M0 0h5v5H0zM7 0h5v5H7zM0 7h5v5H0zM7 7h5v5H7z"/></svg>Human Resource<span class="chev">⌄</span></div>
      <ul class="nav-sub"><li>HR Submenu 1</li><li>HR Submenu 2</li><li>HR Submenu 3</li><li>HR Submenu 4</li></ul>
    </li>
    <li class="nav-item"><svg viewBox="0 0 12 12"><circle cx="6" cy="3.5" r="3"/><path d="M0 12c0-4 3-5 6-5s6 1 6 5z"/></svg>Recruiting<span class="chev">›</span></li>
    <li class="nav-item"><svg viewBox="0 0 12 12"><path d="M0 2h7v1H1v8h8V6h1v6H0zM5 6l6-6 1 1-6 6H5z"/></svg>Inventory<span class="chev">›</span></li>
    <li class="nav-item"><svg viewBox="0 0 12 12"><path d="M0 2h12v1L6 7 0 3zM0 4.5l6 4 6-4V10H0z"/></svg>Contacts<span class="chev">›</span></li>
    <li class="nav-item"><svg viewBox="0 0 12 12"><path d="M5 0a5 5 0 014 8l3 3-1 1-3-3A5 5 0 115 0zm0 2a3 3 0 100 6 3 3 0 000-6z"/></svg>Supervision<span class="chev">›</span></li>
    <li class="nav-item"><svg viewBox="0 0 12 12"><path d="M0 1h12v8H7v1h2v1H3v-1h2V9H0zm1 1v6h10V2z"/></svg>Reports<span class="chev">›</span></li>
    <li class="nav-item"><svg viewBox="0 0 12 12"><circle cx="6" cy="6" r="4.5"/><circle cx="6" cy="6" r="1.8" fill="#1c4a71"/></svg>Settings<span class="chev">›</span></li>
    <li class="nav-item"><svg viewBox="0 0 12 12"><path d="M0 0h1v11h11v1H0zM3 6h2v4H3zM6 3h2v7H6zM9 5h2v5H9z"/></svg>Organisation Charts</li>
  </ul>
</aside>

<section class="welcome">
  <h1>Welcome to Admin + Dashboard</h1>
  <p>Special <strong>Admin theme</strong> for medium and large web applications with very clean and aasethetic style and feel</p>
</section>

<table class="candidates">
  <colgroup><col style="width:72px"><col style="width:85px"><col style="width:86px"><col style="width:90px"><col style="width:95px"><col style="width:80px"><col style="width:80px"><col style="width:90px"><col style="width:80px"><col style="width:73px"><col style="width:74px"><col style="width:101px"></colgroup>
  <thead><tr><th>Created</th><th>Name</th><th>Phone No</th><th>Mobile No</th><th>City, State</th><th>Status</th><th>Notes</th><th>Reason</th><th>Reactive</th><th>Retest</th><th>ReHire</th><th>Job Position</th></tr></thead>
  <tbody>
    <tr><td>23-Jun-2017</td><td>Alex Morgan</td><td>(555)-010-2040</td><td>(555)-010-3197</td><td>Hesperia, California</td><td>Qualified</td><td><a>Notes</a></td><td></td><td></td><td></td><td></td><td>Un-Armed Guard</td></tr>
    <tr><td>23-Jun-2017</td><td>Alex Morgan</td><td>(555)-010-2040</td><td>(555)-010-3197</td><td>Hesperia, California</td><td>Qualified</td><td><a>Notes</a></td><td></td><td></td><td></td><td></td><td>Un-Armed Guard</td></tr>
    <tr><td>23-Jun-2017</td><td>Alex Morgan</td><td>(555)-010-2040</td><td>(555)-010-3197</td><td>Hesperia, California</td><td>Qualified</td><td><a>Notes</a></td><td></td><td></td><td></td><td></td><td>Un-Armed Guard</td></tr>
    <tr><td>23-Jun-2017</td><td>Alex Morgan</td><td>(555)-010-2040</td><td>(555)-010-3197</td><td>Hesperia, California</td><td>Qualified</td><td><a>Notes</a></td><td></td><td></td><td></td><td></td><td>Un-Armed Guard</td></tr>
    <tr><td>23-Jun-2017</td><td>Alex Morgan</td><td>(555)-010-2040</td><td>(555)-010-3197</td><td>Hesperia, California</td><td>Qualified</td><td><a>Notes</a></td><td></td><td></td><td></td><td></td><td>Un-Armed Guard</td></tr>
    <tr><td>23-Jun-2017</td><td>Alex Morgan</td><td>(555)-010-2040</td><td>(555)-010-3197</td><td>Hesperia, California</td><td>Qualified</td><td><a>Notes</a></td><td></td><td></td><td></td><td></td><td>Un-Armed Guard</td></tr>
    <tr><td>23-Jun-2017</td><td>Alex Morgan</td><td>(555)-010-2040</td><td>(555)-010-3197</td><td>Hesperia, California</td><td>Qualified</td><td><a>Notes</a></td><td></td><td></td><td></td><td></td><td>Un-Armed Guard</td></tr>
    <tr><td>23-Jun-2017</td><td>Alex Morgan</td><td>(555)-010-2040</td><td>(555)-010-3197</td><td>Hesperia, California</td><td>Qualified</td><td><a>Notes</a></td><td class="reason"><span class="pill">All</span></td><td></td><td></td><td></td><td>Un-Armed Guard</td></tr>
    <tr><td>23-Jun-2017</td><td>Alex Morgan</td><td>(555)-010-2040</td><td>(555)-010-3197</td><td>Hesperia, California</td><td>Qualified</td><td><a>Notes</a></td><td></td><td></td><td></td><td></td><td>Un-Armed Guard</td></tr>
    <tr><td>23-Jun-2017</td><td>Alex Morgan</td><td>(555)-010-2040</td><td>(555)-010-3197</td><td>Hesperia, California</td><td>Qualified</td><td><a>Notes</a></td><td></td><td></td><td></td><td></td><td>Un-Armed Guard</td></tr>
    <tr><td>23-Jun-2017</td><td>Alex Morgan</td><td>(555)-010-2040</td><td>(555)-010-3197</td><td>Hesperia, California</td><td>Qualified</td><td><a>Notes</a></td><td></td><td></td><td></td><td></td><td>Un-Armed Guard</td></tr>
    <tr><td>23-Jun-2017</td><td>Alex Morgan</td><td>(555)-010-2040</td><td>(555)-010-3197</td><td>Hesperia, California</td><td>Qualified</td><td><a>Notes</a></td><td></td><td></td><td></td><td></td><td>Un-Armed Guard</td></tr>
    <tr><td>23-Jun-2017</td><td>Alex Morgan</td><td>(555)-010-2040</td><td>(555)-010-3197</td><td>Hesperia, California</td><td>Qualified</td><td><a>Notes</a></td><td></td><td></td><td></td><td></td><td>Un-Armed Guard</td></tr>
  </tbody>
</table>

<nav class="pager">
  <span class="pg nav-btn">⏮</span><span class="pg nav-btn">⏴</span>
  <span class="pg current">1</span><span class="pg">2</span><span class="pg">3</span><span class="pg">4</span><span class="pg">5</span><span class="pg">6</span><span class="pg">7</span><span class="pg">8</span>
  <span class="pg nav-btn">⏵</span><span class="pg nav-btn">⏭</span>
  <span class="page-size">Page size <span class="pill">15</span></span>
  <span class="count"><b>3361</b> items in <b>225</b> pages</span>
</nav>

<footer class="footer">
  <span>Copyright Summit Guard Services© 2017, All Rights Reserved</span>
  <span>10GB of <b>250GB</b> Free.</span>
</footer>
</body>
</html>
```